Stonefield Partners Business Card Design

We are looking for a new business card design, we are not happy with our current design. We are a boutique management consulting firm and our clients are typically fortune 500 companies.

I have attached the current front and back that we have as well as a version of our logo that can be used. I am trying to get a higher resolution version of the logo file to upload to the project.

Target Market(s)

Fortune 500 companies are our primary client base. Financial services, life sciences, pharmaceuticals and telecom companies are

Industry/Entity Type

Management Consulting

Contact Information for Business Card

We are trying to communicate a high degree of professionalism, a somewhat minimalist perhaps with some air of whimsy (without overdoing it). Attached is the current design, front and back as well as logos. I like the current back of the card and assume we will keep the phrase the same.

From a color palette perspective, I prefer to stay with a gray scale as they are today.

Font styles to use
Sans Serif

Colors
1b1b1b
474747
ffffff

Requirements
Must have
• Two sided business card design. File format should be something that can be used outside of Photoshop like MS Publisher so that they can be edited with personal information.
• Font should be calibri or something very similar and should be available within MS Office
Should not have
• No other logos or graphics outside of the logo provided.

```html
<!DOCTYPE html>
<html lang="en">
<head>
<meta charset="utf-8">
<title>Stonefield Partners Business Card</title>
<link href="https://fonts.googleapis.com/css2?family=Carlito:wght@400;700&display=swap" rel="stylesheet">
<style>
  :root {
    --page: #ffffff;
    --card-dark: #1b1e22;
    --card-mid: #23282e;
    --band: #3b4651;
    --band-edge: #2c343c;
    --text-light: #e9ecef;
    --text-muted: #9aa3ab;
    --avatar: #4a535c;
  }
  * { margin: 0; padding: 0; box-sizing: border-box; }
  html, body {
    width: 840px; height: 1200px; overflow: hidden;
    background: var(--page);
    font-family: "Carlito", "Calibri", sans-serif;
  }
  .sheet { position: relative; width: 840px; height: 1200px; }

  .card {
    position: absolute; left: 148px; width: 530px; height: 306px;
    background: var(--card-dark);
    overflow: hidden;
  }
  .card-front { top: 266px; }
  .card-back { top: 636px; display: flex; }

  .front-band {
    position: absolute; left: 0; right: 0; top: 78px; height: 128px;
    background: linear-gradient(180deg, var(--band) 0%, var(--band-edge) 100%);
    display: flex; align-items: center; justify-content: center; gap: 18px;
  }
  .brand-dot {
    width: 34px; height: 34px; border-radius: 50%;
    background: var(--text-light);
  }
  .brand-name {
    color: var(--text-light); font-size: 52px; font-weight: 400;
    letter-spacing: 0.5px; white-space: nowrap;
  }

  .back-person {
    width: 265px; height: 100%;
    background: linear-gradient(180deg, #1f2328 0%, var(--card-dark) 100%);
    padding: 52px 0 0 50px;
  }
  .avatar {
    width: 100px; height: 100px; border-radius: 50%;
    background: radial-gradient(circle at 50% 40%, #5a636c, var(--avatar));
  }
  .person-name {
    margin-top: 20px; color: var(--text-light);
    font-size: 30px; font-weight: 400; line-height: 1;
  }
  .person-details {
    margin-top: 10px; list-style: none;
    color: var(--text-muted); font-size: 13px; line-height: 1.65;
  }

  .back-company {
    flex: 1; height: 100%;
    background: var(--card-mid);
    padding: 50px 0 0 80px;
  }
  .company-mark { display: flex; align-items: center; gap: 10px; }
  .company-mark .brand-dot { width: 20px; height: 20px; }
  .company-mark .brand-name { font-size: 26px; }
  .company-details {
    margin-top: 16px; list-style: none;
    color: var(--text-muted); font-size: 13px; line-height: 1.65;
  }
  .company-details .company-title { color: var(--text-light); font-weight: 700; }
</style>
</head>
<body>
<main class="sheet">
  <section class="card card-front" aria-label="Card front">
    <div class="front-band">
      <span class="brand-dot"></span>
      <span class="brand-name">Stonefield Partners</span>
    </div>
  </section>

  <section class="card card-back" aria-label="Card back">
    <div class="back-person">
      <div class="avatar" role="img" aria-label="Portrait photo of the card holder"></div>
      <h1 class="person-name">Daniel Reyes</h1>
      <ul class="person-details">
        <li>Los Angeles Office</li>
        <li>Managing Director</li>
        <li>555.014.2290</li>
        <li>dreyes@stonefieldpartners.com</li>
      </ul>
    </div>
    <div class="back-company">
      <div class="company-mark">
        <span class="brand-dot"></span>
        <span class="brand-name">Stonefield</span>
      </div>
      <ul class="company-details">
        <li class="company-title">Stonefield Partners, Inc.</li>
        <li>Headquarters</li>
        <li>218 Harlow Avenue</li>
        <li>Suite 140</li>
        <li>Cedar Point, WA 98000</li>
      </ul>
    </div>
  </section>
</main>
</body>
</html>
```